FB and Youtube banner design for HVAC company

I would like an appealing site page banner for business page on Facebook (851w x 315h pixels) and one for youtube (2560w x 1440h pixels) for hvac company. Business card design and logo are attached. Company name is Bright Meadow Air Conditioning, Refrigeration, and Heating.

NOTE: I put the business cards and log up to see some of the artwork the company is using. It's not to replicate that in the banner images.

Target Market(s)

Interested business and homeowner visitors to Facebook business page and youtube channel page.

Industry/Entity Type

Hvac

Font styles to use
Sans Serif

Requirements
Must have
• See logo for color scheme.
Should not have
• This should not look like a business card. Think of what is typically the banner on a facebook business page and youtube channel.

```html
<!DOCTYPE html>
<html lang="en">
<head>
<meta charset="utf-8">
<title>Bright Meadow – Social Banners</title>
<link rel="stylesheet" href="https://fonts.googleapis.com/css2?family=Open+Sans:wght@400;600;700&display=swap">
<style>
  :root {
    --orange: #f26a0f;
    --navy: #1c2f6b;
    --blue: #2a4fa6;
    --white: #ffffff;
    --sky: #9fd6e6;
    --sea: #4fb3cf;
    --sand: #e9e3d8;
    --page: #e6e8ea;
    --metal: #c9ccd0;
  }
  * { box-sizing: border-box; margin: 0; padding: 0; }
  html, body { width: 1200px; height: 1200px; overflow: hidden; }
  body {
    background: var(--page);
    font-family: "Open Sans", Arial, sans-serif;
    position: relative;
  }
  .banner { position: absolute; overflow: hidden; background: var(--sand); }
  .banner--facebook { left: 90px; top: 58px; width: 1020px; height: 380px; }
  .banner--youtube { left: 74px; top: 524px; width: 1054px; height: 592px; }

  .banner__scene {
    position: absolute; inset: 0;
    background: linear-gradient(180deg, var(--sky) 0%, var(--sea) 38%, #bfe0e6 50%, var(--sand) 62%, #ddd5c6 100%);
  }
  .banner__bands { position: absolute; inset: 0; width: 100%; height: 100%; }

  .banner__address {
    position: absolute; color: var(--white); font-weight: 400; line-height: 1.2;
  }
  .banner__title {
    position: absolute; color: var(--white); font-weight: 700; letter-spacing: 0.5px;
    line-height: 1; border-bottom: 2px solid var(--navy); padding-bottom: 4px;
    text-shadow: 0 1px 3px rgba(0,0,0,0.15); white-space: nowrap;
  }
  .banner__services {
    position: absolute; color: var(--navy); font-variant: small-caps; font-weight: 400;
    white-space: nowrap;
  }
  .banner__person { position: absolute; text-align: center; }
  .banner__name {
    color: var(--orange); font-weight: 700; border-bottom: 2px solid var(--navy);
    line-height: 1.15; display: inline-block; white-space: nowrap;
  }
  .banner__role { color: var(--navy); font-weight: 400; display: block; }

  .banner__brand {
    position: absolute; display: flex; align-items: center; gap: 12px;
    color: var(--blue); font-weight: 700; white-space: nowrap;
  }
  .banner__brand-dot { border-radius: 50%; background: var(--orange); flex: none; }

  .banner__equipment {
    position: absolute; border-radius: 6px;
    background: linear-gradient(135deg, #f4f5f6 0%, var(--metal) 60%, #8f949a 100%);
  }
  .banner__contacts {
    position: absolute; display: flex; align-items: center; color: var(--white);
    text-transform: uppercase; font-weight: 400; white-space: nowrap;
  }
  .contact { display: flex; align-items: center; gap: 5px; }
  .contact svg { fill: var(--orange); flex: none; }

  /* Facebook sizing */
  .banner--facebook .banner__address { left: 26px; top: 6px; font-size: 17px; }
  .banner--facebook .banner__title { left: 70px; top: 114px; font-size: 46px; }
  .banner--facebook .banner__services { left: 70px; top: 170px; font-size: 22px; }
  .banner--facebook .banner__person { left: 150px; top: 210px; width: 260px; }
  .banner--facebook .banner__name { font-size: 30px; }
  .banner--facebook .banner__role { font-size: 19px; }
  .banner--facebook .banner__brand { left: 672px; top: 86px; font-size: 34px; }
  .banner--facebook .banner__brand-dot { width: 40px; height: 40px; }
  .banner--facebook .banner__equipment { left: 644px; top: 188px; width: 326px; height: 176px; }
  .banner--facebook .banner__contacts { left: 26px; top: 344px; gap: 16px; font-size: 14px; }

  /* YouTube sizing */
  .banner--youtube .banner__address { left: 72px; top: 28px; font-size: 22px; }
  .banner--youtube .banner__title { left: 80px; top: 186px; font-size: 54px; }
  .banner--youtube .banner__services { left: 80px; top: 252px; font-size: 25px; }
  .banner--youtube .banner__person { left: 154px; top: 308px; width: 340px; }
  .banner--youtube .banner__name { font-size: 44px; }
  .banner--youtube .banner__role { font-size: 27px; }
  .banner--youtube .banner__brand { left: 642px; top: 176px; font-size: 38px; }
  .banner--youtube .banner__brand-dot { width: 48px; height: 48px; }
  .banner--youtube .banner__equipment { left: 640px; top: 330px; width: 322px; height: 186px; }
  .banner--youtube .banner__contacts { left: 108px; top: 538px; gap: 28px; font-size: 22px; }
</style>
</head>
<body>

<section class="banner banner--facebook" aria-label="Facebook cover banner">
  <div class="banner__scene" role="img" aria-label="Blurred photo of a sunny beach with turquoise sea and white sand"></div>
  <svg class="banner__bands" viewBox="0 0 1020 380" preserveAspectRatio="none" aria-hidden="true">
    <polygon points="0,0 1020,0 1020,12 0,60" fill="#f26a0f"/>
    <polygon points="0,60 1020,12 1020,17 0,65" fill="#1c2f6b"/>
    <polygon points="0,325 1020,298 1020,380 0,380" fill="#2a4fa6"/>
    <polygon points="0,320 1020,293 1020,298 0,325" fill="#1c2f6b"/>
  </svg>
  <p class="banner__address">PO Box 218 Fairview, NY 11790<br>Lic. H5081234000</p>
  <h1 class="banner__title">BRIGHT MEADOW</h1>
  <p class="banner__services">Air Conditioning, Refrigeration, and Heating</p>
  <p class="banner__person"><span class="banner__name">Daniel Harper</span><span class="banner__role">Mecanic</span></p>
  <div class="banner__brand"><span class="banner__brand-dot"></span>Bright Meadow</div>
  <div class="banner__equipment" role="img" aria-label="Photo of air conditioning units, a furnace and a thermostat"></div>
  <div class="banner__contacts">
    <span class="contact"><svg width="15" height="15" viewBox="0 0 24 24"><path d="M6.6 10.8a15 15 0 0 0 6.6 6.6l2.2-2.2c.3-.3.7-.4 1-.2 1.1.4 2.3.6 3.6.6.6 0 1 .4 1 1V20c0 .6-.4 1-1 1A17 17 0 0 1 3 4c0-.6.4-1 1-1h3.5c.6 0 1 .4 1 1 0 1.3.2 2.5.6 3.6.1.3 0 .7-.2 1z"/></svg>555.013.0142</span>
    <span class="contact"><svg width="15" height="15" viewBox="0 0 24 24"><path d="M2 5h20v14H2z M2 5l10 8 10-8" stroke="#2a4fa6" stroke-width="1.5"/></svg>daniel@bmeadowhvac.com</span>
    <span class="contact"><svg width="15" height="15" viewBox="0 0 24 24"><circle cx="12" cy="12" r="10"/><path d="M2 12h20M12 2c3 3 3 17 0 20M12 2c-3 3-3 17 0 20" stroke="#2a4fa6" stroke-width="1.5" fill="none"/></svg>www.bmeadowhvac.com</span>
  </div>
</section>

<section class="banner banner--youtube" aria-label="YouTube channel banner">
  <div class="banner__scene" role="img" aria-label="Blurred photo of a sunny beach with turquoise sea and white sand"></div>
  <svg class="banner__bands" viewBox="0 0 1054 592" preserveAspectRatio="none" aria-hidden="true">
    <polygon points="0,0 1054,0 1054,68 0,130" fill="#f26a0f"/>
    <polygon points="0,130 1054,68 1054,74 0,136" fill="#1c2f6b"/>
    <polygon points="0,474 1054,426 1054,592 0,592" fill="#2a4fa6"/>
    <polygon points="0,468 1054,420 1054,426 0,474" fill="#1c2f6b"/>
  </svg>
  <p class="banner__address">PO Box 218 Fairview, NY 11790<br>Lic. H5081234000</p>
  <h1 class="banner__title">BRIGHT MEADOW</h1>
  <p class="banner__services">Air Conditioning, Refrigeration, and Heating</p>
  <p class="banner__person"><span class="banner__name">Daniel Harper</span><span class="banner__role">Mecanic</span></p>
  <div class="banner__brand"><span class="banner__brand-dot"></span>Bright Meadow</div>
  <div class="banner__equipment" role="img" aria-label="Photo of air conditioning units, a furnace and a thermostat"></div>
  <div class="banner__contacts">
    <span class="contact"><svg width="22" height="22" viewBox="0 0 24 24"><path d="M6.6 10.8a15 15 0 0 0 6.6 6.6l2.2-2.2c.3-.3.7-.4 1-.2 1.1.4 2.3.6 3.6.6.6 0 1 .4 1 1V20c0 .6-.4 1-1 1A17 17 0 0 1 3 4c0-.6.4-1 1-1h3.5c.6 0 1 .4 1 1 0 1.3.2 2.5.6 3.6.1.3 0 .7-.2 1z"/></svg>555.013.0142</span>
    <span class="contact"><svg width="22" height="22" viewBox="0 0 24 24"><path d="M2 5h20v14H2z M2 5l10 8 10-8" stroke="#2a4fa6" stroke-width="1.5"/></svg>daniel@bmeadowhvac.com</span>
    <span class="contact"><svg width="22" height="22" viewBox="0 0 24 24"><circle cx="12" cy="12" r="10"/><path d="M2 12h20M12 2c3 3 3 17 0 20M12 2c-3 3-3 17 0 20" stroke="#2a4fa6" stroke-width="1.5" fill="none"/></svg>www.bmeadowhvac.com</span>
  </div>
</section>

</body>
</html>
```